Convert my PowerPoint mock up of a hiring process flow to simple, informative illustration with some

I need to create an illustration which is meant to be an overview of a hiring process for a medical training start up. I created a pretty rough PowerPoint mock up that hopefully shows what I am trying to do. My hope is that I would get the illustration created and can add it to my website. I have several other similar projects needed as well and probably ongoing graphic design work if we develop a good working relationship.

Site: www.brolvanhealth.com

Target Market(s)

Medical employers

Industry/Entity Type

Healthcare

Number of Pages Required

1 page

Font styles to use
Serif
Sans Serif

Colors
2fb6a2
85cae6

Requirements
Must have
• Simple illustration when done
Nice to have
• Fits very well with existing look and feel of site.
Should not have
• Not sure

```html
<!DOCTYPE html>
<html lang="en">
<head>
<meta charset="utf-8">
<title>Brolvan – Hiring Process</title>
<link href="https://fonts.googleapis.com/css2?family=Open+Sans:wght@300;400;600&display=swap" rel="stylesheet">
<style>
:root{
  --teal:#2fb6a2;
  --teal-light:#3fcdb6;
  --sky:#85cae6;
  --sky-dark:#64b4d8;
  --orange:#fba52a;
  --orange-dark:#e58a06;
  --navy:#1f5e8c;
  --green:#1d6f3a;
  --ink:#4a4a4a;
  --panel:rgba(70,140,170,.35);
  --panel-line:rgba(150,205,230,.45);
  --white:#fff;
}
*{box-sizing:border-box;margin:0;padding:0}
html,body{width:1200px;height:932px;overflow:hidden}
body{font-family:'Open Sans',sans-serif;background:var(--white);position:relative;color:var(--white)}
.header{position:absolute;left:0;top:0;width:1200px;height:93px;background:var(--white)}
.brand{position:absolute;left:99px;top:34px;display:flex;align-items:center;gap:8px;color:var(--navy);font-size:22px;font-weight:600;letter-spacing:.5px}
.brand-mark{width:14px;height:14px;background:var(--navy)}
.nav{position:absolute;top:38px;left:0;font-size:13px;color:var(--ink)}
.nav a{position:absolute;white-space:nowrap;color:var(--ink);text-decoration:none}
.hero{position:absolute;left:0;top:93px;width:1200px;height:773px;background:linear-gradient(135deg,#3f6f8a 0%,#6f98ad 45%,#4d7c96 70%,#2f5d78 100%)}
.panel{position:absolute;top:189px;width:457px;height:599px;background:var(--panel);border:1px solid var(--panel-line);border-radius:3px}
.abs{position:absolute}
.frame{position:absolute;border:1px solid var(--panel-line);border-radius:2px;padding:3px}
.csv{width:100%;height:100%;background:linear-gradient(#8fd0ec,var(--sky-dark));display:flex;align-items:center;justify-content:center;font-weight:300;font-size:25px}
.photo{width:100%;height:100%;background:linear-gradient(#b9b2a8,#6e6a66)}
.heading{font-weight:300;font-size:25px;line-height:35px;text-align:center}
.copy{border:1px solid var(--panel-line);border-radius:2px;font-size:11px;line-height:24px;text-align:center;padding:28px 30px;display:flex;align-items:center}
.step{display:flex;align-items:center;justify-content:center;text-align:center;font-weight:300;font-size:21px;line-height:27px;border-radius:2px}
.step.teal{background:linear-gradient(var(--teal-light),var(--teal))}
.step.sky{background:linear-gradient(#8fd0ec,var(--sky-dark))}
.step.orange{background:linear-gradient(var(--orange),var(--orange-dark))}
.tip{position:absolute;bottom:-10px;left:50%;margin-left:-10px;width:0;height:0;border-left:10px solid transparent;border-right:10px solid transparent}
.tip.teal{border-top:10px solid var(--teal)}
.tip.sky{border-top:10px solid var(--sky-dark)}
.footer{position:absolute;left:0;top:866px;width:1200px;height:66px;background:var(--white);text-align:center;font-size:11px;color:var(--ink);padding-top:26px}
.footer span{margin:0 7px}
</style>
</head>
<body>
<header class="header">
  <div class="brand"><span class="brand-mark"></span>Brolvan</div>
  <nav class="nav">
    <a style="left:825px">Home</a>
    <a style="left:921px">About Us</a>
    <a style="left:1037px">Contact Us</a>
  </nav>
</header>

<section class="hero" role="img" aria-label="Blurred photo of a medical professional at work in a laboratory"></section>

<div class="panel" style="left:99px">
  <div class="frame" style="left:17px;top:18px;width:80px;height:83px"><div class="csv">CSV</div></div>
  <div class="frame" style="left:103px;top:18px;width:80px;height:83px"><div class="csv">CSV</div></div>
  <div class="frame" style="left:189px;top:18px;width:80px;height:83px"><div class="csv">CSV</div></div>
  <div class="frame" style="left:275px;top:18px;width:80px;height:83px"><div class="csv">CSV</div></div>
  <div class="frame" style="left:361px;top:18px;width:80px;height:83px"><div class="csv">CSV</div></div>
  <div class="heading abs" style="left:0;top:126px;width:457px">Collect and Synthesize Candidates<br>for Training, Employment</div>
  <div class="copy abs" style="left:17px;top:214px;width:423px;height:162px">Lorem Ipsum is simply dummy text of the printing and typesetting industry. Lorem Ipsum has been the industry's standard dummy text ever since the 1500s, when an unknown printer took a galley of type and scrambled it to make a type specimen book. It has survived not only five centuries, but also the leap...</div>
  <div class="step teal abs" style="left:17px;top:395px;width:423px;height:76px">Employer selects their favored<br>candidates to interview<span class="tip teal"></span></div>
  <div class="frame" style="left:17px;top:497px;width:80px;height:84px"><div class="photo" role="img" aria-label="Candidate portrait"></div></div>
  <div class="frame" style="left:103px;top:497px;width:80px;height:84px"><div class="photo" role="img" aria-label="Candidate portrait"></div></div>
  <div class="frame" style="left:189px;top:497px;width:80px;height:84px"><div class="photo" role="img" aria-label="Candidate portrait"></div></div>
  <div class="frame" style="left:275px;top:497px;width:80px;height:84px"><div class="photo" role="img" aria-label="Candidate portrait"></div></div>
  <div class="frame" style="left:361px;top:497px;width:80px;height:84px"><div class="photo" role="img" aria-label="Candidate portrait"></div></div>
</div>

<svg class="abs" style="left:557px;top:446px" width="86" height="86" viewBox="0 0 86 86" aria-hidden="true">
  <path d="M0 0 L18 0 L43 43 L18 86 L0 86 L25 43Z M43 0 L61 0 L86 43 L61 86 L43 86 L68 43Z" fill="var(--sky-dark)"/>
</svg>

<div class="panel" style="left:645px">
  <div class="step sky abs" style="left:17px;top:17px;width:423px;height:77px">Employer, Brolvan agree upon<br>training protocol<span class="tip sky"></span></div>
  <div class="step teal abs" style="left:17px;top:129px;width:423px;height:57px">Candidates interviewed by Employer</div>
  <div class="frame" style="left:17px;top:199px;width:80px;height:84px"><div class="photo" role="img" aria-label="Interviewee portrait"></div></div>
  <div class="frame" style="left:103px;top:199px;width:80px;height:84px"><div class="photo" role="img" aria-label="Interviewee portrait"></div></div>
  <div class="frame" style="left:189px;top:199px;width:80px;height:84px"><div class="photo" role="img" aria-label="Interviewee portrait"></div></div>
  <svg class="abs" style="left:285px;top:213px" width="64" height="64" viewBox="0 0 86 86" aria-hidden="true">
    <path d="M0 0 L18 0 L43 43 L18 86 L0 86 L25 43Z M43 0 L61 0 L86 43 L61 86 L43 86 L68 43Z" fill="var(--sky)"/>
  </svg>
  <div class="frame" style="left:360px;top:199px;width:80px;height:84px"><div class="photo" role="img" aria-label="Finalist portrait"></div></div>
  <div class="step sky abs" style="left:17px;top:292px;width:251px;height:51px">Interviews<span class="tip sky"></span></div>
  <div class="step sky abs" style="left:360px;top:292px;width:80px;height:51px">Finalist<span class="tip sky"></span></div>
  <div class="step teal abs" style="left:17px;top:369px;width:423px;height:57px">Brolvan Pre-Employment Training</div>
  <div class="step orange abs" style="left:128px;top:444px;width:200px;height:57px">Start Job!</div>
  <div class="step teal abs" style="left:17px;top:522px;width:423px;height:57px">Post Employment Support (1-3 months)</div>
</div>

<footer class="footer">© 2015. Brolvan Health.All rights reserved.<span></span>Terms &amp; Conditions<span>/</span>Privacy policy<span>/</span>Disclaimer</footer>
</body>
</html>
```